General Contractor Website Design

We are working with a General Contractor in California that specializes in building custom kitchens, baths, and homes for high-end clients.

Here are some websites for inspiration:
https://morvelstudio.example/
https://ridgelanebuildworks.example
https://www.framequill.example
https://www.nestiva.example
https://www.tzdwell.example
https://rplresidences.example

Thank you for taking the time to consider designing a website for us. We are web developers based in Stockton, CA, USA. Most of our projects go through the same process. Understanding this process may help you win a project with us. We custom-code all of our websites in-house. We don’t have any requirements as to what tools you use for your design, but we ask that you follow these guidelines.

IMAGES:
If you use any images or icons in the design, we ask that you have a link to the asset so we can purchase the image/icon. Most of the designs we submit do not have the customer’s images on them unless they have some great images. Be creative; show us the feeling you are trying to portray with your image choices. Use any royalty-free site you choose. We subscribe to Velqor and mainly use their images, but we can purchase images outside of Velqor. PLEASE NOTE: we will not submit designs to clients with watermarks on the images.

FONTS:
We ask that you identify the fonts you’re using in the design. This can be done in a message if you want. We typically use Google Fonts and Velqor Fonts.

CONTENT:
We're always open to different content and ideas. We often submit designs with stock images so the client can see our vision. We typically take pictures after the website launch to use their images with our vision. Lorem Ipsum is fine for paragraphs, but we ask that you make the Headers with correct English. We want to be able to show the vision and identify the sections of the website.

INSPIRATION:
We typically add a couple of links in the brief of websites we like to help you get started in your design.

REVISIONS:
We do not often ask for revisions of the designs unless we see something in the design that may not appeal to the client. If there are slight changes that we want to make, we do that in the development process.

FEEDBACK:
We rarely give feedback on designs during the design process. We are working on many website projects and do not have the time to provide feedback. We usually respond if your request is well thought out and asks specific questions, but a note asking “feedback, please” usually goes unanswered.

```html
<!DOCTYPE html>
<html lang="en">
<head>
<meta charset="utf-8">
<title>Ashford Builtworks — Custom Kitchens, Baths and Homes</title>
<link rel="stylesheet" href="https://fonts.googleapis.com/css2?family=Oswald:wght@600;700&family=Nunito:wght@800&family=Lato:wght@400;700&display=swap">
<style>
:root{
  --red:#e31b32;
  --red-deep:#c8142a;
  --black:#0b0b0b;
  --ink:#151515;
  --footer-head:#2a0b10;
  --white:#ffffff;
  --line:#8a0f1d;
}
*{box-sizing:border-box;margin:0;padding:0}
html,body{width:1200px;height:3656px;overflow:hidden;background:var(--white)}
body{position:relative;font-family:"Lato",sans-serif;color:var(--ink)}
.abs{position:absolute}
.photo{position:absolute;display:block;overflow:hidden}

/* header */
.site-header{position:absolute;left:0;top:0;width:1200px;height:102px;background:var(--white);box-shadow:0 1px 3px rgba(0,0,0,.08)}
.brand{position:absolute;left:54px;top:32px;display:flex;align-items:center;gap:10px}
.brand-mark{width:38px;height:38px;background:var(--red)}
.brand-name{font-family:"Lato",sans-serif;font-weight:700;font-size:22px;letter-spacing:2.5px;color:var(--red);text-transform:uppercase;line-height:38px}
.main-nav{position:absolute;top:37px;left:513px;display:flex;gap:39px;font-size:19px;color:var(--ink)}
.search-icon{position:absolute;left:1103px;top:38px}

/* hero */
.hero{left:0;top:102px;width:1200px;height:469px;
  background:
    radial-gradient(ellipse 260px 200px at 330px 190px,rgba(255,250,225,.95),rgba(255,250,225,0) 70%),
    radial-gradient(ellipse 320px 120px at 620px 330px,rgba(222,196,150,.85),rgba(222,196,150,0) 75%),
    radial-gradient(ellipse 200px 140px at 900px 150px,rgba(200,200,204,.7),rgba(200,200,204,0) 70%),
    linear-gradient(180deg,#e9e7e2 0%,#f4f2ec 38%,#dcd6c9 62%,#c9b48e 78%,#bfb9ae 100%)}

/* explore */
.explore-dark{left:0;top:571px;width:1200px;height:372px;
  background:
    radial-gradient(ellipse 700px 220px at 600px 120px,rgba(40,40,40,.7),rgba(0,0,0,0) 70%),
    linear-gradient(180deg,#141414,#050505)}
.red-field{left:0;top:943px;width:1200px;height:939px;background:linear-gradient(160deg,var(--red) 0%,var(--red-deep) 100%)}
.section-title{position:absolute;left:0;width:1200px;text-align:center;font-family:"Oswald",sans-serif;font-weight:700;font-size:58px;letter-spacing:1px;text-transform:uppercase}
.explore-title{top:648px;color:var(--white)}
.project-card{top:756px;width:347px;height:394px;box-shadow:0 4px 8px rgba(0,0,0,.35)}
.card-label{left:486px;top:1070px;width:231px;height:47px;background:var(--red);color:var(--white);font-size:36px;text-align:center;line-height:47px}
.btn{position:absolute;width:228px;height:46px;background:var(--black);color:var(--white);font-size:23px;text-align:center;line-height:46px;box-shadow:0 3px 6px rgba(0,0,0,.4)}

/* about */
.about-heading{left:694px;top:1310px;width:490px;font-family:"Nunito",sans-serif;font-weight:800;font-size:34px;line-height:59px;color:var(--white)}
.about-text{left:694px;top:1561px;width:480px;font-size:19px;line-height:39px;color:var(--white)}

/* video */
.video{left:0;top:1882px;width:1200px;height:516px;
  background:
    radial-gradient(ellipse 420px 140px at 600px 340px,rgba(150,70,50,.9),rgba(150,70,50,0) 75%),
    radial-gradient(ellipse 300px 120px at 250px 380px,rgba(140,60,45,.8),rgba(140,60,45,0) 75%),
    radial-gradient(ellipse 300px 120px at 960px 380px,rgba(140,60,45,.8),rgba(140,60,45,0) 75%),
    linear-gradient(180deg,#54604f 0%,#3b3d40 28%,#6b4c3e 50%,#5b4236 70%,#4a6a34 86%,#3f6a2a 100%)}
.video::after{content:"";position:absolute;inset:0;background:rgba(0,0,0,.28)}
.play{left:527px;top:2050px}

/* gallery */
.gallery-title{top:2440px;color:var(--ink)}
.gallery-item{width:339px;height:342px}

/* footer */
.site-footer{left:0;top:3324px;width:1200px;height:255px;background:var(--red)}
.footer-col{position:absolute;top:3372px;color:var(--white);font-size:20px;line-height:28px}
.footer-col h3{font-family:"Lato",sans-serif;font-weight:700;font-size:24px;letter-spacing:1px;color:var(--footer-head);line-height:30px;margin-bottom:2px}
.footer-col ul{list-style:none;padding-left:3px}
.socials{display:flex;gap:10px;margin-top:14px;padding-left:5px}
.socials span{width:30px;height:30px;background:var(--black);border-radius:4px}
.copyright{left:0;top:3579px;width:1200px;height:77px;background:var(--red);border-top:2px solid var(--line);color:var(--white);text-align:center;font-size:20px;line-height:75px}
</style>
</head>
<body>

<header class="site-header">
  <div class="brand"><span class="brand-mark"></span><span class="brand-name">Ashford Builtworks</span></div>
  <nav class="main-nav"><span>Home</span><span>Our Firm</span><span>Our Services</span><span>Portfolio</span><span>Contact</span></nav>
  <svg class="search-icon" width="26" height="26" viewBox="0 0 26 26"><circle cx="10.5" cy="10.5" r="8" fill="none" stroke="#111" stroke-width="3.5"/><line x1="16.5" y1="16.5" x2="24" y2="24" stroke="#111" stroke-width="4" stroke-linecap="round"/></svg>
</header>

<div class="photo hero" role="img" aria-label="Bright white custom kitchen with glass-front cabinets, steel range hood and marble island"></div>

<section>
  <div class="abs explore-dark" role="img" aria-label="Dark damask patterned band"></div>
  <div class="abs red-field"></div>
  <h2 class="section-title explore-title">Explore Projects</h2>
  <div class="photo project-card" style="left:38px;background:radial-gradient(ellipse 140px 90px at 174px 230px,rgba(255,214,140,.85),rgba(255,214,140,0) 75%),linear-gradient(180deg,#2f4d8c 0%,#8fa0c0 22%,#e6e4de 42%,#d8d2c4 66%,#5a4a36 76%,#3f7a2a 86%,#2f5e1e 100%)" role="img" aria-label="Two-storey white family home lit at dusk"></div>
  <div class="photo project-card" style="left:428px;background:radial-gradient(ellipse 150px 110px at 170px 130px,rgba(255,255,255,1),rgba(255,255,255,0) 75%),linear-gradient(180deg,#f4f4f2 0%,#e2e2df 40%,#c8c9c8 60%,#e8dcc6 75%,#f0efeb 100%)" role="img" aria-label="White kitchen with pendant lights and steel appliances"></div>
  <div class="abs card-label">kitchens</div>
  <div class="photo project-card" style="left:816px;background:radial-gradient(ellipse 120px 160px at 260px 140px,rgba(255,236,205,.8),rgba(255,236,205,0) 75%),linear-gradient(120deg,#3a2f27 0%,#7d6450 30%,#a48b70 55%,#d7cbbb 78%,#b59c80 100%)" role="img" aria-label="Modern bathroom with freestanding tub and wood wall panels"></div>
  <div class="btn" style="left:487px;top:1203px">See More</div>
</section>

<section>
  <div class="photo" style="left:37px;top:1300px;width:377px;height:460px;background:linear-gradient(180deg,#1e2124 0%,#2f3338 20%,#8a6241 38%,#2a2b2d 58%,#7e5a3b 75%,#d9cfbf 90%,#e7e0d4 100%)" role="img" aria-label="Dark kitchen with charcoal tiles and wood cabinetry"></div>
  <div class="photo" style="left:293px;top:1385px;width:377px;height:460px;background:radial-gradient(ellipse 90px 160px at 250px 200px,rgba(240,240,238,.9),rgba(240,240,238,0) 75%),linear-gradient(180deg,#f1f2f3 0%,#dfe2e6 14%,#2c4a74 30%,#8a8a86 46%,#2d4770 62%,#dcdcda 80%,#efefee 100%);box-shadow:0 4px 10px rgba(0,0,0,.35)" role="img" aria-label="Navy blue galley kitchen with marble floor"></div>
  <h2 class="abs about-heading">We believe in a future with thoughtfully designed and well-built homes<br>for everyone.</h2>
  <p class="abs about-text">Contrary to popular belief, Lorem Ipsum is not simply random text. It has roots in a piece of classical Latin literature from 45 BC, making it over 2000 years old.<br>Harlan Vesper, a Latin professor at<br>Brookmere College in Vermont,</p>
  <div class="btn" style="left:838px;top:1803px">See More</div>
</section>

<section>
  <div class="abs video" role="img" aria-label="Video still of a red brick family home with green lawn"></div>
  <svg class="abs play" width="132" height="132" viewBox="0 0 132 132"><circle cx="66" cy="66" r="61" fill="none" stroke="#fff" stroke-width="6"/><polygon points="52,40 52,92 94,66" fill="#fff"/></svg>
</section>

<section>
  <h2 class="section-title gallery-title">Our Project Gallery</h2>
  <div class="photo gallery-item" style="left:39px;top:2543px;background:linear-gradient(180deg,#f2f1ee 0%,#e8e3da 35%,#d5c6b0 52%,#ebe9e4 64%,#c79a64 78%,#e9e7e2 100%)" role="img" aria-label="Kitchen island with marble top and wooden stools"></div>
  <div class="photo gallery-item" style="left:428px;top:2543px;background:linear-gradient(90deg,#f4f4f3 0%,#ecebe8 45%,#c9c8c5 70%,#8d8b87 100%)" role="img" aria-label="White bathroom with glass shower and soaking tub"></div>
  <div class="photo gallery-item" style="left:824px;top:2543px;background:linear-gradient(180deg,#4e86d6 0%,#a9c4e6 30%,#f1f1f1 46%,#c9a27a 62%,#3e3e40 72%,#6a8a4a 86%,#4a6e2a 100%)" role="img" aria-label="Modern white house with wood cladding and garage"></div>
  <div class="photo gallery-item" style="left:39px;top:2939px;background:radial-gradient(ellipse 110px 50px at 170px 240px,rgba(250,246,238,.95),rgba(250,246,238,0) 80%),linear-gradient(180deg,#5e4b36 0%,#a6a48e 24%,#8e8a6a 42%,#7a6550 56%,#c8b49a 72%,#b89f82 100%)" role="img" aria-label="Freestanding bathtub before a wide landscape window"></div>
  <div class="photo gallery-item" style="left:428px;top:2939px;background:linear-gradient(180deg,#4f7d94 0%,#9ab8c2 36%,#3a86a8 50%,#c9d6d8 64%,#5a8a3c 82%,#3d6a24 100%)" role="img" aria-label="Cottage with blue roof on a green lawn"></div>
  <div class="photo gallery-item" style="left:824px;top:2939px;background:linear-gradient(180deg,#d8cfbe 0%,#e6dfcf 30%,#b9ab92 52%,#8f8a84 64%,#1f1d1b 76%,#c9bca6 100%)" role="img" aria-label="Cream kitchen with dark granite countertops"></div>
</section>

<footer>
  <div class="abs site-footer"></div>
  <div class="footer-col" style="left:97px">
    <h3>CONTACT US</h3>
    <ul>
      <li>Larkspur Row 41, Eastvale, Oregon, USA</li>
      <li>www.ashfordbuiltworks.example</li>
      <li>(+1) 0100-555-0199</li>
    </ul>
    <div class="socials"><span></span><span></span><span></span><span></span><span></span><span></span></div>
  </div>
  <div class="footer-col" style="left:596px">
    <h3>INFORMATION</h3>
    <ul><li>Product Support</li><li>Checkout</li><li>Report Abuse</li><li>Redeem Voucher</li><li>Order Status</li></ul>
  </div>
  <div class="footer-col" style="left:908px">
    <h3>USEFUL LINKS</h3>
    <ul><li>Policies &amp; Rules</li><li>Privacy Policy</li><li>License Policy</li><li>My Account</li><li>Locality</li></ul>
  </div>
  <div class="abs copyright">© 2023 All Rights Reserved. By ashfordbuiltworks</div>
</footer>

</body>
</html>
```